Re-design of veterinary clinic website *

For a future relaunch of our webpage, we would like to find a fresh design that still incorporates the spirit of our current one which can be found at http://dr-kolmsand.de
We are a small business that appeals to locals but are known in a wide area for specialist services.
According to analytics data, most people rarely read through the full website but are using it to inform themselves about opening hours, Telephone numbers and location. Still, the website needs to offer enough content to be ranked positively by the Vextora algorithm.
Our logo is not part of the re-design but needs to be included in your proposal as is. It can be used a source of inspiration, just as the current design. Keep in mind, that the design will be used as the basis of a fluid webdesign for both mobile and desktop. Roughly 75% of our users are on mobile devices.
Target Market(s)
Locals
Industry/Entity Type
Veterinary
Number of Pages Required
1 page
Look and feel
Each slider illustrates characteristics of the customer's brand and the style your logo design should communicate.

```html
<!DOCTYPE html>
<html lang="de">
<head>
<meta charset="utf-8">
<title>Client Review – Dr. Kolmsand</title>
<link href="https://fonts.googleapis.com/css2?family=Mulish:wght@400;600;700&family=Arimo:wght@400;700&display=swap" rel="stylesheet">
<style>
  :root{
    --section-bg:#ededed;
    --card-bg:#ffffff;
    --heading:#111111;
    --body-grey:#9a9a9a;
    --name-grey:#6b6b6b;
    --quote-grey:#8a8a8a;
    --accent-blue:#8cc8ec;
    --footer-bg:#062340;
    --bar-bg:#0c2b4c;
    --label-blue:#6fc3ea;
    --white:#ffffff;
    --link-blue:#9dd8f5;
    --logo-navy:#24338a;
    --top-btn:#2fb9e6;
    --social-1:#3bb3ea;
    --social-2:#4a7bd0;
    --social-3:#e3503f;
    --social-4:#2f4776;
  }
  *{margin:0;padding:0;box-sizing:border-box}
  html,body{width:1200px;height:1000px;overflow:hidden}
  body{position:relative;background:var(--section-bg);font-family:"Mulish",sans-serif}

  .reviews{position:absolute;left:0;top:0;width:1200px;height:454px;background:var(--section-bg)}
  .reviews__paw{position:absolute;left:621px;top:-14px;width:34px;height:28px;border-radius:50%;background:var(--accent-blue)}
  .reviews__title{position:absolute;top:24px;left:70px;width:1130px;text-align:center;font-weight:400;font-size:35px;color:var(--heading)}

  .review{position:absolute;top:85px;width:312px}
  .review__card{position:relative;height:187px;background:var(--card-bg);font-family:"Arimo",sans-serif}
  .review__tail{position:absolute;left:40px;top:187px}
  .review__mark{position:absolute;font-family:"Arimo",sans-serif;font-weight:700;font-size:22px;line-height:1;color:var(--quote-grey)}
  .review__mark--open{left:39px;top:16px}
  .review__mark--close{left:228px;top:146px}
  .review__text{position:absolute;left:40px;top:40px;width:226px;font-size:11px;line-height:20px;color:var(--body-grey)}
  .review__avatar{position:absolute;left:0;top:229px;width:64px;height:64px;border:2px solid var(--white);background:linear-gradient(135deg,#d9b98a,#6f5a3e 70%,#3b3a30)}
  .review__name{position:absolute;left:80px;top:239px;font-family:"Arimo",sans-serif;font-weight:700;font-size:13px;color:var(--name-grey);text-transform:uppercase}
  .review__role{position:absolute;left:80px;top:260px;font-family:"Arimo",sans-serif;font-weight:700;font-size:11px;color:var(--body-grey)}

  .footer{position:absolute;left:0;top:454px;width:1200px;height:464px;background:var(--footer-bg)}
  .footer__brand{position:absolute;left:182px;top:57px;width:868px;height:128px;border-radius:12px;background:var(--white);display:flex;align-items:center;justify-content:center;gap:18px}
  .footer__brand-dot{width:34px;height:34px;border-radius:50%;background:var(--logo-navy)}
  .footer__brand-name{font-family:"Mulish",sans-serif;font-weight:700;font-size:30px;letter-spacing:1px;color:var(--logo-navy)}

  .footer__col{position:absolute;top:244px;color:var(--white);font-size:15px;font-weight:600;line-height:24px}
  .footer__col--address{right:631px;text-align:right}
  .footer__col--contact{left:629px;top:246px}
  .footer__label{font-weight:700;font-size:14px;color:var(--label-blue);text-transform:uppercase;margin-bottom:5px}

  .social{position:absolute;top:356px;left:508px;display:flex;gap:13px}
  .social__item{width:36px;height:36px;border-radius:50%}
  .social__item--a{background:var(--social-1)}
  .social__item--b{background:var(--social-2)}
  .social__item--c{background:var(--social-3)}
  .social__item--d{background:var(--social-4)}

  .to-top{position:absolute;left:1140px;top:400px;width:40px;height:40px;border-radius:50%;background:var(--top-btn);display:flex;align-items:center;justify-content:center}

  .copyright{position:absolute;left:0;top:918px;width:1200px;height:82px;padding-left:98px;background:var(--bar-bg);color:var(--white);font-size:19px;text-align:center;line-height:76px}
  .copyright a{color:var(--link-blue);text-decoration:none}
</style>
</head>
<body>
  <section class="reviews">
    <div class="reviews__paw"></div>
    <h2 class="reviews__title">Client Review</h2>

    <article class="review" style="left:105px">
      <div class="review__card">
        <span class="review__mark review__mark--open">&ldquo;</span>
        <p class="review__text">Lorem Ipsum is simply dummy text of the printing and typesetting industry. Lorem Ipsum has been the industry's standard dummy text ever since the 1500s, when an unknown printer took a galley</p>
        <span class="review__mark review__mark--close">&rdquo;</span>
      </div>
      <svg class="review__tail" width="32" height="30" viewBox="0 0 32 30"><polygon points="0,0 32,0 0,30" fill="#ffffff"/></svg>
      <div class="review__avatar" role="img" aria-label="Client photo with dog"></div>
      <div class="review__name">Jacy Doe</div>
      <div class="review__role">Assistant Manager</div>
    </article>

    <article class="review" style="left:461px">
      <div class="review__card">
        <span class="review__mark review__mark--open">&ldquo;</span>
        <p class="review__text">Lorem Ipsum is simply dummy text of the printing and typesetting industry. Lorem Ipsum has been the industry's standard dummy text ever since the 1500s, when an unknown printer took a galley</p>
        <span class="review__mark review__mark--close">&rdquo;</span>
      </div>
      <svg class="review__tail" width="32" height="30" viewBox="0 0 32 30"><polygon points="0,0 32,0 0,30" fill="#ffffff"/></svg>
      <div class="review__avatar" role="img" aria-label="Client photo with dog"></div>
      <div class="review__name">Roy Doe</div>
      <div class="review__role">Business Manager</div>
    </article>

    <article class="review" style="left:801px">
      <div class="review__card">
        <span class="review__mark review__mark--open">&ldquo;</span>
        <p class="review__text">Lorem Ipsum is simply dummy text of the printing and typesetting industry. Lorem Ipsum has been the industry's standard dummy text ever since the 1500s, when an unknown printer took a galley</p>
        <span class="review__mark review__mark--close">&rdquo;</span>
      </div>
      <svg class="review__tail" width="32" height="30" viewBox="0 0 32 30"><polygon points="0,0 32,0 0,30" fill="#ffffff"/></svg>
      <div class="review__avatar" role="img" aria-label="Client photo with dog"></div>
      <div class="review__name">Roy Doe</div>
      <div class="review__role">Business Manager</div>
    </article>
  </section>

  <footer class="footer">
    <div class="footer__brand">
      <span class="footer__brand-dot"></span>
      <span class="footer__brand-name">Henrik Kolmsand</span>
    </div>

    <div class="footer__col footer__col--address">
      <div class="footer__label">Clinic Address</div>
      <div>Birkenallee 7</div>
      <div>10999 Musterstadt (Nordviertel)</div>
    </div>

    <div class="footer__col footer__col--contact">
      <div class="footer__label">Contact Us</div>
      <div>Telefon: 030 / 555 01 23</div>
      <div>Telefax: 030 / 555 01 24</div>
    </div>

    <nav class="social" aria-label="Social links">
      <span class="social__item social__item--a"></span>
      <span class="social__item social__item--b"></span>
      <span class="social__item social__item--c"></span>
      <span class="social__item social__item--d"></span>
    </nav>

    <a class="to-top" href="#" aria-label="Back to top">
      <svg width="12" height="8" viewBox="0 0 12 8"><polyline points="2,6 6,2 10,6" fill="none" stroke="#ffffff" stroke-width="2"/></svg>
    </a>
  </footer>

  <div class="copyright">All right reserved <a href="http://dr-kolmsand.de">dr-kolmsand.de</a>. Copyright 2019-20</div>
</body>
</html>
```